Lab & Medical Equipment Repair Company Business Card Design

Looking for business card design for a lab & medical equipment repair company. Must be double-sided and must list our primary pieces we repair. Optionally, can include a QR code which should direct to our website.

Clients are usually doctors, so the card must be designed with a professional tone; however, we are looking for creativity in presentation. Open as to what should be on the front and back on card.

** Looking for a CLEAN design with creativity. Please use "Nice to have Priorities" items with discretion.

Core marketing logic:

When lab or medical equipment needs repair, most doctors call the manufacturers and schedule a technician to repair. Usually this takes one or two weeks, and, often, their work spoils. Alternatively, the doctors could hold equipment insurance which gives them a less expensive cost, but the response time is still similarly long.

Our company provides both competitive rates and one of the fastest response times in the industry. Technicians are dispatched directly to the site of the equipment, usually within 24 hours. Equipment under contract receives the same fast response time and includes complimentary annual maintenance. We service some of the most prestigious facilities in the Pittsburgh area and cover all of Western Pennsylvania, Ohio, and West Virginia.

Target Market(s)

Laboratory owners (doctors)

Industry/Entity Type

Marketing

Requirements
Must have
• Company Logo
Employee Name: Ray Dunwoody
Employee Title: CEO
Company Phone: 724-555-0187
Company Fax: 866-555-0143
Company Address: PO Box 518 Harmony Glen, PA 16099
Company Website: www.brightfixlabtech.example
Equipment We Service: Freezers, Cryostorage, Incubators, Centrifuges, Refrigerators, Environmental Chambers, Autoclaves, and more.

Nice to have
• Company Facebook: social.example/bfltllc
Company Twitter: @BFLTLLC
QR Code (link to website): www.brightfixlabtech.example

```html
<!DOCTYPE html>
<html lang="en">
<head>
<meta charset="utf-8">
<title>BFLT Business Card – Front and Back</title>
<link href="https://fonts.googleapis.com/css2?family=Open+Sans:wght@400;600;700&display=swap" rel="stylesheet">
<style>
  :root {
    --ink: #000000;
    --paper: #ffffff;
    --brand-green: #22a84a;
    --crop-grey: #9a9a9a;
    --social-mark-a: #4a6aa8;
    --social-mark-b: #6fb6e0;
  }
  * { box-sizing: border-box; margin: 0; padding: 0; }
  html, body { width: 1200px; height: 900px; overflow: hidden; background: var(--paper); }
  body { position: relative; font-family: "Open Sans", Arial, sans-serif; color: var(--ink); }

  .side-label { position: absolute; left: 0; width: 1200px; text-align: center; font-size: 24px; font-weight: 400; line-height: 1; }
  .side-label--front { top: 26px; }
  .side-label--back { top: 462px; }

  .crop { position: absolute; background: var(--crop-grey); }
  .crop--v { width: 1px; height: 43px; }
  .crop--h { height: 1px; width: 43px; }

  .el { position: absolute; }

  /* Front */
  .name-bar { left: 350px; top: 141px; width: 244px; height: 75px; background: var(--ink); color: var(--paper); padding: 14px 0 0 32px; }
  .name-bar__name { font-size: 16px; font-weight: 700; line-height: 24px; }
  .name-bar__title { font-size: 14px; font-weight: 400; line-height: 24px; }

  .logo { left: 604px; top: 141px; width: 216px; height: 75px; display: flex; align-items: center; justify-content: center; gap: 12px; }
  .logo__mark { width: 14px; height: 14px; background: var(--brand-green); }
  .logo__name { font-size: 46px; font-weight: 700; letter-spacing: 6px; color: var(--ink); line-height: 1; }
  .end-bar { left: 830px; top: 141px; width: 20px; height: 75px; background: var(--ink); }

  .contact { top: 292px; font-size: 14px; line-height: 24px; }
  .contact--address { left: 382px; }
  .contact--lines { right: 382px; text-align: right; }
  .contact__label { color: var(--brand-green); }
  .contact__heading { color: var(--brand-green); font-weight: 700; }

  .green-band { left: 350px; top: 368px; width: 500px; height: 17px; background: var(--brand-green); }

  /* Back */
  .back-panel { left: 350px; top: 535px; width: 500px; height: 235px; background: var(--ink); text-align: center; padding-top: 136px; }
  .back-panel__heading { color: var(--paper); font-size: 16px; font-weight: 700; line-height: 24px; }
  .back-panel__list { color: var(--brand-green); font-size: 14px; line-height: 24px; letter-spacing: 0.2px; }

  .social { left: 350px; top: 777px; width: 500px; text-align: center; font-size: 14px; line-height: 24px; display: flex; justify-content: center; align-items: center; gap: 4px; }
  .social__mark { width: 18px; height: 18px; display: inline-block; }
  .social__mark--a { background: var(--social-mark-a); }
  .social__mark--b { background: var(--social-mark-b); }
  .social__divider { margin: 0 8px; color: var(--ink); }
  .base-bar { left: 350px; top: 805px; width: 500px; height: 17px; background: var(--ink); }
</style>
</head>
<body>
  <div class="side-label side-label--front">FRONT</div>

  <div class="crop crop--v" style="left:350px;top:50px"></div>
  <div class="crop crop--v" style="left:849px;top:50px"></div>
  <div class="crop crop--h" style="left:300px;top:99px"></div>
  <div class="crop crop--h" style="left:857px;top:99px"></div>
  <div class="crop crop--h" style="left:300px;top:385px"></div>
  <div class="crop crop--h" style="left:857px;top:385px"></div>
  <div class="crop crop--v" style="left:350px;top:392px"></div>
  <div class="crop crop--v" style="left:849px;top:392px"></div>

  <section class="card card--front" aria-label="Card front">
    <div class="el name-bar">
      <div class="name-bar__name">Ray Dunwoody</div>
      <div class="name-bar__title">CEO</div>
    </div>
    <div class="el logo">
      <span class="logo__name">BFLT</span>
      <span class="logo__mark"></span>
    </div>
    <div class="el end-bar"></div>

    <div class="el contact contact--address">
      <div class="contact__heading">Address:</div>
      <div>PO Box 518 Harmony Glen</div>
      <div>PA 16099</div>
    </div>
    <div class="el contact contact--lines">
      <div><span class="contact__label">Phone:</span> 724-555-0187</div>
      <div><span class="contact__label">Fax:</span> 866-555-0143</div>
      <div>www.brightfixlabtech.example</div>
    </div>
    <div class="el green-band"></div>
  </section>

  <div class="side-label side-label--back">BACK</div>

  <div class="crop crop--v" style="left:350px;top:486px"></div>
  <div class="crop crop--v" style="left:849px;top:486px"></div>
  <div class="crop crop--h" style="left:300px;top:535px"></div>
  <div class="crop crop--h" style="left:857px;top:535px"></div>
  <div class="crop crop--h" style="left:300px;top:822px"></div>
  <div class="crop crop--h" style="left:857px;top:822px"></div>
  <div class="crop crop--v" style="left:350px;top:828px"></div>
  <div class="crop crop--v" style="left:849px;top:828px"></div>

  <section class="card card--back" aria-label="Card back">
    <div class="el back-panel">
      <div class="back-panel__heading">Equipment We Service</div>
      <div class="back-panel__list">Freezers, Cryostorage, Incubators, Centrifuges, Refrigerators</div>
      <div class="back-panel__list">Environmental Chambers, Autoclaves, and more.</div>
    </div>
    <div class="el social">
      <span class="social__mark social__mark--a" aria-hidden="true"></span>
      <span>: social.example/bfltllc</span>
      <span class="social__divider">|</span>
      <span class="social__mark social__mark--b" aria-hidden="true"></span>
      <span>: @BFLTLLC</span>
    </div>
    <div class="el base-bar"></div>
  </section>
</body>
</html>
```